Business Card Design

A business card design must match as a cleaning company.
We do house cleaning, office, cafe , function center , club and so on.

Industry/Entity Type

House

Contact Information for Business Card

Brightmere Cleaning Services
Marla Voss
Director
0491570156
1300 975 708
Brightmere.cleaning@example.com

```html
<!DOCTYPE html>
<html lang="en">
<head>
<meta charset="utf-8">
<title>Brightmere Cleaning Services – Business Card</title>
<link rel="stylesheet" href="https://fonts.googleapis.com/css2?family=Quicksand:wght@500;600;700&display=swap">
<style>
  :root {
    --brand-blue: #0410cc;
    --slate: #4f5a5b;
    --paper: #ffffff;
  }
  * { margin: 0; padding: 0; box-sizing: border-box; }
  html, body {
    width: 1200px;
    height: 741px;
    overflow: hidden;
    background: var(--paper);
  }
  .card {
    position: relative;
    width: 1200px;
    height: 741px;
    background: var(--paper);
    font-family: "Quicksand", sans-serif;
    text-align: center;
  }
  .brand-mark {
    position: absolute;
    top: 135px;
    left: 0;
    width: 100%;
    height: 150px;
    display: flex;
    justify-content: center;
    align-items: center;
    gap: 24px;
  }
  .brand-mark__dot {
    width: 150px;
    height: 150px;
    display: block;
    flex: none;
  }
  .brand-mark__name {
    font-weight: 600;
    font-size: 50px;
    color: var(--slate);
  }
  .company-band {
    position: absolute;
    top: 359px;
    left: 0;
    width: 100%;
    height: 68px;
    background: var(--brand-blue);
    display: flex;
    align-items: center;
    justify-content: center;
  }
  .company-band__name {
    color: var(--paper);
    font-weight: 600;
    font-size: 42px;
    line-height: 1;
  }
  .person {
    position: absolute;
    top: 455px;
    left: 0;
    width: 100%;
  }
  .person__name {
    font-weight: 600;
    font-size: 36px;
    color: var(--slate);
    line-height: 44px;
  }
  .person__role {
    font-weight: 600;
    font-size: 22px;
    color: var(--brand-blue);
    line-height: 30px;
  }
  .contact {
    position: absolute;
    top: 561px;
    left: 0;
    width: 100%;
    list-style: none;
    font-weight: 600;
    font-size: 24px;
    color: var(--slate);
    line-height: 33px;
  }
</style>
</head>
<body>
  <div class="card">
    <div class="brand-mark">
      <svg class="brand-mark__dot" viewBox="0 0 150 150" aria-hidden="true">
        <circle cx="75" cy="75" r="75" fill="var(--slate)"/>
      </svg>
      <span class="brand-mark__name">Brightmere</span>
    </div>

    <div class="company-band">
      <h1 class="company-band__name">Brightmere Cleaning Services</h1>
    </div>

    <div class="person">
      <h2 class="person__name">Marla Voss</h2>
      <p class="person__role">Director</p>
    </div>

    <ul class="contact">
      <li class="contact__mobile">0491570156</li>
      <li class="contact__phone">1300 975 708</li>
      <li class="contact__email">Brightmere.cleaning@example.com</li>
    </ul>
  </div>
</body>
</html>
```